Website for Lucent Prose Advisory Group

Please design a website that initially contains four or five pages. This work is for a newly formed consulting company, Lucent Prose Advisory Group, that provides training and individual coaching to help business professionals and lawyers write more effectively and efficiently.

We work in a professional and conservative industry. The website should be simple, crisp, and clean.

I have attached a document that describes the four initial pages for the site: 1) a landing page, 2) a webpage that includes the pictures and bios of our two consultants, 3) a webpage that describes our services, and 4) a webpage that will contain a form that visitors can use to submit questions to us.

I also included the following files:
a. a powerpoint slide with our consultants' pictures and bios; and
b. our recently designed logo (jpg and png files).

Thank you!

```html
<!DOCTYPE html>
<html lang="en">
<head>
<meta charset="utf-8">
<title>Lucent Prose Advisory Group</title>
<link href="https://fonts.googleapis.com/css2?family=Poppins:wght@400;500;700;800&display=swap" rel="stylesheet">
<style>
:root{
  --red:#c3262f;
  --ink:#2b2b2b;
  --text:#3a3a3a;
  --dark-bar:#222222;
  --white:#ffffff;
  --hero-a:#5b5d62;
  --hero-b:#3f3b38;
}
*{margin:0;padding:0;box-sizing:border-box}
html,body{width:1200px;height:2238px;overflow:hidden}
body{position:relative;font-family:"Poppins",sans-serif;color:var(--text);background:var(--white)}
.site-header{position:absolute;left:0;top:0;width:1200px;height:136px;background:var(--white)}
.brand{position:absolute;left:76px;top:46px;display:flex;align-items:center;gap:10px;font-weight:500;font-size:22px;color:var(--ink)}
.brand-mark{width:12px;height:12px;background:var(--red)}
.main-nav{position:absolute;top:52px;left:0;width:1200px}
.main-nav a{position:absolute;font-size:13.5px;color:var(--text);text-decoration:none}
.main-nav a.active{color:var(--red)}
.hero{position:absolute;left:0;top:136px;width:1200px;height:838px;background:linear-gradient(160deg,#77797d 0%,var(--hero-a) 45%,var(--hero-b) 100%)}
.hero-title{position:absolute;left:0;top:556px;width:1200px;text-align:center;color:var(--white);font-weight:800;font-size:53px;line-height:64px;letter-spacing:-1px;text-transform:uppercase;text-shadow:2px 3px 4px rgba(0,0,0,.45)}
.intro-brand{position:absolute;left:0;top:1100px;width:1200px;text-align:center;font-weight:500;font-size:35px;line-height:46px;color:var(--ink)}
.welcome{position:absolute;left:76px;top:1214px;width:560px}
.welcome h2{font-weight:500;font-size:22px;color:var(--red);line-height:34px}
.welcome .dot{display:block;width:3px;height:3px;background:var(--red);border-radius:50%;margin:4px 0 8px 1px}
.welcome p{font-size:13.6px;line-height:22.6px;color:var(--text);margin-bottom:22.6px;white-space:nowrap}
.accent-block{position:absolute;left:1019px;top:1163px;width:181px;height:582px;background:var(--red)}
.photo{position:absolute;border:7px solid var(--white)}
.photo-handshake{left:769px;top:1224px;width:351px;height:463px;background:linear-gradient(170deg,#a9a19a 0%,#6f6862 50%,#e5e2de 100%)}
.photo-meeting{left:636px;top:1424px;width:330px;height:308px;background:linear-gradient(175deg,#cfd9dd 0%,#8f7a66 55%,#b88a5c 100%)}
.site-footer{position:absolute;left:0;top:1854px;width:1200px;height:312px;background:var(--red);color:var(--white)}
.footer-col{position:absolute;top:62px}
.footer-col h3{font-weight:500;font-size:18px;line-height:24px}
.footer-col h3::after{content:"";display:block;width:36px;height:2px;background:var(--white);margin-top:5px}
.quick-links{left:258px}
.quick-links ul{list-style:none;margin-top:36px}
.quick-links li{display:flex;align-items:center;gap:10px;height:27px;font-size:13.5px}
.contact-list{left:463px}
.contact-item{position:absolute;left:0;display:flex;gap:18px;align-items:flex-start;width:260px}
.contact-icon{width:27px;height:27px;border:1px solid var(--white);border-radius:3px;display:flex;align-items:center;justify-content:center;flex:none}
.contact-text{font-size:13.5px;line-height:16px}
.newsletter{left:760px}
.newsletter p{font-size:13.5px;line-height:18px;margin-top:42px;width:230px}
.newsletter .email-field{display:block;width:218px;height:34px;background:var(--white);border:0;margin-top:16px}
.newsletter .subscribe{display:block;background:none;border:0;color:var(--white);font-family:"Poppins",sans-serif;font-size:11px;margin:22px 0 0 24px}
.copyright{position:absolute;left:0;top:2166px;width:1200px;height:72px;background:var(--dark-bar);color:var(--white);font-size:13px;text-align:center;line-height:72px}
</style>
</head>
<body>
<header class="site-header">
  <div class="brand"><span class="brand-mark"></span>Lucent Prose Advisory Group</div>
  <nav class="main-nav">
    <a class="active" style="left:621px">Home</a>
    <a style="left:713px">About Us</a>
    <a style="left:820px">Consultants</a>
    <a style="left:948px">Services</a>
    <a style="left:1051px">Contact us</a>
  </nav>
</header>

<section class="hero" role="img" aria-label="Photo of a group of young professionals gathered around a laptop">
  <h1 class="hero-title">Training and individual coaching<br>to help business professionals<br>and lawyers</h1>
</section>

<div class="intro-brand">Lucent Prose Advisory Group</div>

<section class="welcome">
  <h2>Welcome to Lucent Prose Advisory Group</h2>
  <span class="dot"></span>
  <p>We train and coach business professionals and lawyers on strategies and<br>techniques to engage, inform, and persuade their readers. We teach our clients<br>that precisely understanding their readers’ concerns and motivations leads<br>them to select the<br>appropriate tone, to develop the most effective narrative, and to make the<br>complicated judgments necessary for effective written communication.</p>
  <p>We tangibly improved the written product of business professionals and<br>lawyers at corporations and elite law firms by tailoring our training and<br>coaching to our client’s particular objectives and characteristics. As educators,<br>our training methodology involves assessing our client’s culture, the<br>writing requirements and skills of its professionals, and the expectations of its<br>leadership. From there, we tailor our training program and coaching<br>emphases.</p>
  <p>We hone our message to fit each client and each assignment.</p>
</section>

<div class="accent-block"></div>
<div class="photo photo-handshake" role="img" aria-label="Photo of two businessmen shaking hands in an office"></div>
<div class="photo photo-meeting" role="img" aria-label="Photo of a team meeting around a conference table with laptops"></div>

<footer class="site-footer">
  <div class="footer-col quick-links">
    <h3>Quick Links</h3>
    <ul>
      <li><svg width="14" height="18" viewBox="0 0 14 18" aria-hidden="true"><path d="M12 1 L2 17" stroke="#fff" stroke-width="2.5" stroke-linecap="round"/></svg>Home</li>
      <li><svg width="14" height="18" viewBox="0 0 14 18" aria-hidden="true"><path d="M12 1 L2 17" stroke="#fff" stroke-width="2.5" stroke-linecap="round"/></svg>About Us</li>
      <li><svg width="14" height="18" viewBox="0 0 14 18" aria-hidden="true"><path d="M12 1 L2 17" stroke="#fff" stroke-width="2.5" stroke-linecap="round"/></svg>Consultants</li>
      <li><svg width="14" height="18" viewBox="0 0 14 18" aria-hidden="true"><path d="M12 1 L2 17" stroke="#fff" stroke-width="2.5" stroke-linecap="round"/></svg>Services</li>
      <li><svg width="14" height="18" viewBox="0 0 14 18" aria-hidden="true"><path d="M12 1 L2 17" stroke="#fff" stroke-width="2.5" stroke-linecap="round"/></svg>Contact Us</li>
    </ul>
  </div>

  <div class="footer-col contact-list">
    <h3>Contact Us</h3>
    <div class="contact-item" style="top:75px">
      <span class="contact-icon"><svg width="12" height="12" viewBox="0 0 24 24" aria-hidden="true"><path d="M6.6 10.8a15 15 0 0 0 6.6 6.6l2.2-2.2a1 1 0 0 1 1-.25 11.4 11.4 0 0 0 3.6.57 1 1 0 0 1 1 1V20a1 1 0 0 1-1 1A17 17 0 0 1 3 4a1 1 0 0 1 1-1h3.5a1 1 0 0 1 1 1c0 1.25.2 2.45.57 3.6a1 1 0 0 1-.25 1z" fill="#fff"/></svg></span>
      <div class="contact-text">CALL US<br>8015 550 2718</div>
    </div>
    <div class="contact-item" style="top:124px">
      <span class="contact-icon"><svg width="12" height="10" viewBox="0 0 24 18" aria-hidden="true"><rect x="1" y="1" width="22" height="16" fill="#fff"/><path d="M1 1 L12 10 L23 1" stroke="#c3262f" stroke-width="2" fill="none"/></svg></span>
      <div class="contact-text">EMAIL US<br>hello@lucentprose.com</div>
    </div>
    <div class="contact-item" style="top:173px">
      <span class="contact-icon"><svg width="10" height="14" viewBox="0 0 20 28" aria-hidden="true"><path d="M10 0a10 10 0 0 1 10 10c0 7-10 18-10 18S0 17 0 10A10 10 0 0 1 10 0z" fill="#fff"/><circle cx="10" cy="10" r="3.5" fill="#c3262f"/></svg></span>
      <div class="contact-text">Address line Dummy Here<br>Address line Here</div>
    </div>
  </div>

  <div class="footer-col newsletter">
    <h3>Our Newsletter</h3>
    <p>Subscribe our newsletter to get the latest news.</p>
    <input class="email-field" type="email" aria-label="Email address">
    <button class="subscribe">SUBSCRIBE</button>
  </div>
</footer>

<div class="copyright">Copyright © 2024 All Rights Reserved By Company name</div>
</body>
</html>
```